Business Card for Pottery and Jewellery Designer

A new business card design is needed to accompany a newly launching pottery and jewellery website. The company logo has been attached for use. The company is called Glazewick Studio. For a sense of the vibe please see the website (it is currently under construction but this way you'll get a feel for the style) www.GlazewickStudio.com

The website font is Pontano Sans for the body of the text with Overlock for headers.

The overall look should be clean and elegant. The back side can have just the logo. The front side should have a smaller logo and the following details displayed:

Glazewick Studio
Designer: Hollis Marrow
Phone: xxx.xxx.xxxx
Email: Designer@GlazewickStudio.com

The structure of displaying this is completely up to you. Different layouts and creative methods of displaying contact info are welcome as long as it stays clean/uncluttered.

No product photographs are to be included in the design as the catalogue changes quickly.

Colour preferences lean towards elegant and understated (charcoal grey, dark navy blue etc.)

Please let me know if you have any further questions or further details required.

Target Market(s)

Target market is 30+ year old women

Industry/Entity Type

Construction

Colors
ffffff
1b1b1b
474747
d9d9d9
fafafa
0355a3

Requirements
Must have
• The submissions so far have looked very typical and don't stand out right now. They're also all in navy with very little variation. I'm looking for something that stands out a it more while still being clean-looking.
Nice to have
• I've attached a few design samples and an idea for a backdrop. It would be great to see some designs in black, white, and grey with only a hint of color.
Should not have
• Product Images

```html
<!DOCTYPE html>
<html lang="en">
<head>
<meta charset="utf-8">
<title>Glazewick Studio – Business Card</title>
<link rel="stylesheet" href="https://fonts.googleapis.com/css2?family=Open+Sans:wght@300;400&family=Poppins:wght@600;700&display=swap">
<style>
  :root {
    --backdrop: #161616;
    --card: #fafafa;
    --charcoal: #1b1b1b;
    --graphite: #474747;
    --mist: #d9d9d9;
    --white: #ffffff;
    --accent: #0355a3;
    --card-shadow: rgba(0, 0, 0, 0.55);
  }
  * { box-sizing: border-box; margin: 0; padding: 0; }
  html, body {
    width: 1200px;
    height: 800px;
    overflow: hidden;
    background: var(--backdrop);
  }
  .canvas {
    position: relative;
    width: 1200px;
    height: 800px;
  }
  .card {
    position: absolute;
    width: 500px;
    height: 286px;
    background: var(--card);
    box-shadow: 0 14px 30px var(--card-shadow);
    overflow: hidden;
  }

  /* Back side */
  .card--back { left: 90px; top: 120px; }
  .back-brand {
    position: absolute;
    left: 0; right: 0; top: 0; bottom: 0;
    display: flex;
    flex-direction: column;
    align-items: center;
    justify-content: center;
    padding-top: 40px;
  }
  .brand-mark {
    display: flex;
    align-items: center;
    gap: 14px;
  }
  .brand-dot {
    width: 40px;
    height: 40px;
    border-radius: 50%;
    background: var(--accent);
    flex-shrink: 0;
  }
  .brand-name {
    font-family: "Poppins", sans-serif;
    font-weight: 700;
    font-size: 34px;
    color: var(--charcoal);
    letter-spacing: 0.2px;
    white-space: nowrap;
  }
  .back-url {
    margin-top: 10px;
    font-family: "Poppins", sans-serif;
    font-weight: 700;
    font-size: 15px;
    color: var(--graphite);
    letter-spacing: 0.6px;
  }

  /* Front side */
  .card--front { left: 610px; top: 390px; }
  .name-band {
    position: absolute;
    left: 0; right: 0; top: 0;
    height: 124px;
    background: var(--charcoal);
    padding: 34px 30px 0 0;
    text-align: right;
  }
  .person-name {
    font-family: "Open Sans", sans-serif;
    font-weight: 300;
    font-size: 40px;
    line-height: 1;
    color: var(--white);
  }
  .person-role {
    margin-top: 6px;
    font-family: "Poppins", sans-serif;
    font-weight: 700;
    font-size: 14px;
    color: var(--mist);
    letter-spacing: 0.6px;
  }
  .contact-list {
    position: absolute;
    right: 30px;
    top: 142px;
    list-style: none;
    text-align: right;
    font-family: "Poppins", sans-serif;
    font-weight: 700;
    color: var(--graphite);
  }
  .contact-list li { font-size: 13.5px; line-height: 1.55; letter-spacing: 0.3px; white-space: nowrap; }
  .contact-list .contact-phone { font-size: 17px; letter-spacing: 1.5px; color: var(--charcoal); }
  .front-brand {
    position: absolute;
    left: 26px;
    bottom: 26px;
    display: flex;
    align-items: center;
    gap: 8px;
  }
  .front-brand .brand-dot { width: 22px; height: 22px; }
  .front-brand .brand-name { font-size: 16px; }
</style>
</head>
<body>
  <main class="canvas">
    <section class="card card--back" aria-label="Business card back">
      <div class="back-brand">
        <div class="brand-mark">
          <span class="brand-dot" aria-hidden="true"></span>
          <span class="brand-name">Glazewick Studio</span>
        </div>
        <p class="back-url">www.glazewickstudio.com</p>
      </div>
    </section>

    <section class="card card--front" aria-label="Business card front">
      <header class="name-band">
        <h1 class="person-name">Hollis Marrow</h1>
        <p class="person-role">Designer</p>
      </header>
      <ul class="contact-list">
        <li class="contact-phone">xxx.xxx.xxxx</li>
        <li class="contact-email">Designer@GlazewickStudio.com</li>
        <li class="contact-web">www.glazewickstudio.com</li>
      </ul>
      <div class="front-brand">
        <span class="brand-dot" aria-hidden="true"></span>
        <span class="brand-name">Glazewick Studio</span>
      </div>
    </section>
  </main>
</body>
</html>
```